Desk Allies Business Card

Contact Information for Business Card

Janne Voutilainen
Managing Director

3/47 Brindle Street Mitchell ACT 2911

Tel: +61 02 6257 3140
Mob: +61 0427 315 846

Email: janne@deskallies.com.au
Web: www.deskallies.com.au

Colors

Designer to choose colors to be used in the design.

Requirements
Must have
• Logo, Name, Title, Address, Telephone, Mobile, Email Address and Website
• "Desk Ally International Pty Ltd"

```html
<!DOCTYPE html>
<html lang="en">
<head>
<meta charset="utf-8">
<title>Desk Allies Business Card</title>
<link rel="stylesheet" href="https://fonts.googleapis.com/css2?family=Montserrat:wght@400;500;600;700&display=swap">
<style>
  :root {
    --stage: #2b2d31;
    --card-white: #ffffff;
    --brand-blue: #1677c4;
    --ink-black: #1b1c1e;
    --tag-grey: #6d6f73;
    --text-dark: #222326;
  }
  * { box-sizing: border-box; margin: 0; padding: 0; }
  html, body { width: 1200px; height: 900px; overflow: hidden; }
  body {
    background: var(--stage);
    font-family: "Montserrat", sans-serif;
    position: relative;
  }
  .card {
    position: absolute;
    width: 540px;
    height: 310px;
    border-radius: 22px;
    overflow: hidden;
  }
  .card-front { left: 40px; top: 380px; background: var(--card-white); }
  .card-back { left: 620px; top: 170px; background: var(--brand-blue); }
  .card-shapes { position: absolute; inset: 0; }

  .brand { position: absolute; left: 36px; top: 30px; }
  .brand-row { display: flex; align-items: center; gap: 12px; }
  .brand-dot { width: 34px; height: 34px; border-radius: 50%; background: var(--brand-blue); }
  .brand-name {
    font-weight: 700; font-size: 33px; color: var(--brand-blue);
    text-transform: uppercase; letter-spacing: 0.5px; line-height: 1;
  }
  .brand-tagline {
    margin: 6px 0 0 46px; font-size: 11.5px; letter-spacing: 3.2px;
    color: var(--tag-grey); text-transform: uppercase; font-weight: 500;
  }

  .person { position: absolute; left: 36px; top: 108px; }
  .person-name { font-weight: 700; font-size: 17px; color: var(--text-dark); text-transform: uppercase; }
  .person-name .surname { color: var(--brand-blue); }
  .person-title { font-size: 12.5px; color: var(--text-dark); margin-top: 2px; }

  .phones { position: absolute; left: 22px; top: 190px; color: #fff; font-size: 12px; line-height: 24px; }
  .contact-line { display: flex; align-items: center; gap: 9px; }
  .contact-line svg { width: 12px; height: 12px; flex: none; }

  .online { position: absolute; left: 285px; top: 160px; color: var(--text-dark); font-size: 12.5px; line-height: 21px; }

  .company { position: absolute; left: 210px; top: 238px; color: #fff; font-size: 13px; line-height: 21px; }
  .company-name { font-weight: 700; }

  .back-brand {
    position: absolute; left: 0; right: 0; top: 136px; text-align: center;
    font-weight: 700; font-size: 34px; color: #fff; text-transform: uppercase; letter-spacing: 0.5px;
  }
</style>
</head>
<body>

<section class="card card-front" aria-label="Business card front">
  <svg class="card-shapes" viewBox="0 0 540 310" aria-hidden="true">
    <path d="M0 165 H150 Q178 165 178 193 V310 H0 Z" fill="var(--ink-black)"/>
    <path d="M178 310 V243 Q178 218 203 218 H540 V310 Z" fill="var(--brand-blue)"/>
  </svg>

  <header class="brand">
    <div class="brand-row">
      <span class="brand-dot"></span>
      <span class="brand-name">Desk Allies</span>
    </div>
    <p class="brand-tagline">Ergonomic Office Environments</p>
  </header>

  <div class="person">
    <p class="person-name">Janne <span class="surname">Voutilainen</span></p>
    <p class="person-title">Managing Director</p>
  </div>

  <div class="phones">
    <p class="contact-line">
      <svg viewBox="0 0 12 12"><path d="M2.5 1 L4.5 1 L5 3.5 L3.8 4.4 Q4.8 6.8 7.6 8.2 L8.5 7 L11 7.5 L11 9.5 Q11 11 9.5 11 Q1 10 1 2.5 Q1 1 2.5 1 Z" fill="#fff"/></svg>
      +61 02 6257 3140
    </p>
    <p class="contact-line">
      <svg viewBox="0 0 12 12"><rect x="3" y="0.8" width="6" height="10.4" rx="1.2" fill="none" stroke="#fff" stroke-width="1.2"/><circle cx="6" cy="9.3" r="0.6" fill="#fff"/></svg>
      +61 0427 315 846
    </p>
  </div>

  <div class="online">
    <p class="contact-line">
      <svg viewBox="0 0 12 12"><rect x="0.5" y="2" width="11" height="8" rx="1" fill="var(--brand-blue)"/><path d="M1 2.6 L6 6.6 L11 2.6" fill="none" stroke="#fff" stroke-width="1"/></svg>
      janne@deskallies.com.au
    </p>
    <p class="contact-line">
      <svg viewBox="0 0 12 12"><circle cx="6" cy="6" r="5.3" fill="var(--brand-blue)"/><path d="M0.8 6 H11.2 M6 0.8 Q2.8 6 6 11.2 M6 0.8 Q9.2 6 6 11.2" fill="none" stroke="#fff" stroke-width="0.8"/></svg>
      www.deskallies.com.au
    </p>
  </div>

  <div class="company">
    <p class="company-name">Desk Ally International Pty Ltd</p>
    <p>3/47 Brindle Street Mitchell ACT 2911</p>
  </div>
</section>

<section class="card card-back" aria-label="Business card back">
  <svg class="card-shapes" viewBox="0 0 540 310" aria-hidden="true">
    <circle cx="280" cy="155" r="230" fill="var(--ink-black)"/>
  </svg>
  <p class="back-brand">Desk Allies</p>
</section>

</body>
</html>
```